Business card design for Birch Engineering Torvant

We need a new business card design along with all the necessary to place an order. The company is Birch Engineering Torvant and we recently updated our logo.

```html
<!DOCTYPE html>
<html lang="en">
<head>
<meta charset="UTF-8">
<title>Birch Engineering Torvant — Business Card</title>
<link rel="stylesheet" href="https://fonts.googleapis.com/css2?family=Montserrat:wght@400;500;600&display=swap">
<style>
  :root {
    --stage: #1c1c1f;
    --card: #2a2b2e;
    --card-deep: #232427;
    --card-tone: #313236;
    --wordmark: #a3a3a3;
    --text: #e8e8e8;
    --accent: #e8c21c;
  }
  * { box-sizing: border-box; margin: 0; padding: 0; }
  html, body {
    width: 1200px; height: 800px; overflow: hidden;
    background: var(--stage);
    font-family: "Montserrat", sans-serif;
  }
  .stage {
    width: 1200px; height: 800px;
    display: flex; align-items: center; justify-content: center; gap: 40px;
  }
  .card {
    position: relative;
    width: 540px; height: 310px;
    border-radius: 18px;
    background: var(--card);
    overflow: hidden;
    box-shadow: 0 18px 40px rgba(0,0,0,.45);
  }
  .card__pattern {
    position: absolute; inset: 0;
    background: linear-gradient(135deg, var(--card-tone) 0%, var(--card) 55%, var(--card-deep) 100%);
  }
  .brand {
    position: relative;
    display: flex; align-items: center; gap: 12px;
  }
  .brand__mark {
    width: 14px; height: 14px; background: var(--accent); flex: none;
  }
  .brand__name {
    color: var(--wordmark);
    font-weight: 600;
    font-size: 26px;
    letter-spacing: 1px;
    text-transform: uppercase;
    line-height: 1.15;
  }

  /* front */
  .card--front { display: flex; flex-direction: column; align-items: center; justify-content: center; gap: 26px; }
  .card--front .brand__name { text-align: left; }
  .front__url {
    position: relative;
    color: var(--text); font-size: 12px; letter-spacing: 3.5px;
  }

  /* back */
  .card--back .card__pattern {
    left: auto; width: 60%;
    background: linear-gradient(120deg, var(--card) 0%, var(--card-tone) 60%, var(--card) 100%);
  }
  .card--back .brand { position: absolute; left: 60px; top: 70px; }
  .card--back .brand__name { font-size: 30px; }
  .holder { position: absolute; left: 36px; top: 196px; }
  .holder__name { color: var(--text); font-weight: 600; font-size: 15px; letter-spacing: .5px; text-transform: uppercase; }
  .holder__role { color: var(--accent); font-size: 12px; margin-top: 2px; }
  .rule { position: absolute; left: 36px; right: 28px; top: 240px; height: 1px; background: var(--accent); }
  .contacts {
    position: absolute; left: 36px; right: 28px; top: 252px;
    display: flex; align-items: center; gap: 12px;
    color: var(--text); font-size: 11.5px;
  }
  .contacts__item { display: flex; align-items: center; gap: 6px; }
  .contacts__sep { color: var(--text); opacity: .8; }
  .contacts svg { width: 13px; height: 13px; flex: none; }
  .band { position: absolute; left: 0; right: 0; bottom: 0; height: 8px; background: var(--accent); }
</style>
</head>
<body>
<main class="stage">
  <section class="card card--front">
    <div class="card__pattern" role="img" aria-label="Faint repeating geometric pattern across the card face"></div>
    <div class="brand">
      <span class="brand__mark"></span>
      <span class="brand__name">Birch Engineering<br>Torvant</span>
    </div>
    <p class="front__url">www.birchtorvant.co</p>
  </section>

  <section class="card card--back">
    <div class="card__pattern" role="img" aria-label="Large faint angular decoration in dark grey tones"></div>
    <div class="brand">
      <span class="brand__mark"></span>
      <span class="brand__name">Birch Engineering<br>Torvant</span>
    </div>
    <div class="holder">
      <p class="holder__name">Maren T. Holt</p>
      <p class="holder__role">Partner</p>
    </div>
    <div class="rule"></div>
    <div class="contacts">
      <span class="contacts__item">
        <svg viewBox="0 0 14 14" aria-hidden="true"><rect x="3" y="1" width="8" height="12" rx="1.5" fill="none" stroke="#e8c21c" stroke-width="1.4"/><circle cx="7" cy="11" r=".8" fill="#e8c21c"/></svg>
        0145 872 369
      </span>
      <span class="contacts__sep">|</span>
      <span class="contacts__item">
        <svg viewBox="0 0 14 14" aria-hidden="true"><rect x="1" y="3" width="12" height="8" fill="#e8c21c"/><path d="M1 3l6 5 6-5" fill="none" stroke="#2a2b2e" stroke-width="1.1"/></svg>
        info@birchtorvant.co
      </span>
      <span class="contacts__sep">|</span>
      <span class="contacts__item">
        <svg viewBox="0 0 14 14" aria-hidden="true"><circle cx="7" cy="7" r="5.5" fill="none" stroke="#e8c21c" stroke-width="1.2"/><ellipse cx="7" cy="7" rx="2.4" ry="5.5" fill="none" stroke="#e8c21c" stroke-width="1"/><path d="M1.5 7h11" stroke="#e8c21c" stroke-width="1"/></svg>
        www.birchtorvant.co
      </span>
    </div>
    <div class="band"></div>
  </section>
</main>
</body>
</html>
```